skincare creams for tired moms

I need a package and a logo design for a skincare company based in California called Dawn Meadow. I make day and night cream, under eye cream, and body lotion. The first product I plan to launch is an under eye cream. It does not have to be in these colors but I do teals, greens, black, and cobalt blue.

The package is going to either be in a box or a bag. Either way I go it will be like a gift box or bag. The design should make the person feel like they are getting something special and luxurious just for them.

I have small kids and it is really difficult to find a chunk of time to myself to update or review.

Target Market(s)

mainly first time moms. I am making an under eye cream that does not use retinol but is still powerful enough to get rid of bags and dark circles.

Industry/Entity Type

Cosmetics

Logo Text

The package and logo should incorporate the name Dawn Meadow.

Font styles to use
Decorative
Script

Colors

Designer to choose colors to be used in the design.

Requirements
Nice to have
• maybe focus more on Meadow instead of Dawn. Also incorporate plants or flowers
Should not have
• not a huge fan of pink

```html
<!DOCTYPE html>
<html lang="en">
<head>
<meta charset="utf-8">
<title>Dawn Meadow – Under Eye Cream Box Dieline</title>
<link rel="stylesheet" href="https://fonts.googleapis.com/css2?family=Marcellus+SC&family=Open+Sans:wght@400;600&display=swap">
<style>
  :root {
    --canvas: #ffffff;
    --board: #1a1b1d;
    --fold: #3c3d40;
    --gold: #e0a24a;
    --gold-soft: #f1c27c;
    --ink-light: #ffffff;
  }
  html, body {
    margin: 0;
    padding: 0;
    overflow: hidden;
    background: var(--canvas);
  }
  .dieline {
    display: block;
    width: 1200px;
    height: 1000px;
  }
  .board { fill: var(--board); }
  .fold-line { stroke: var(--fold); stroke-width: 1; fill: none; }
  .gold-rule { stroke: var(--gold); stroke-width: 2; }
  .brand-mark-dot { fill: none; stroke: var(--gold); stroke-width: 1.5; }
  .brand-name {
    font-family: "Marcellus SC", serif;
    font-size: 14px;
    fill: var(--gold);
    letter-spacing: 0.5px;
  }
  .product-name {
    font-family: "Open Sans", sans-serif;
    font-weight: 600;
    font-size: 9.5px;
    fill: var(--ink-light);
  }
  .net-weight {
    font-family: "Open Sans", sans-serif;
    font-weight: 400;
    font-size: 9px;
    fill: var(--gold-soft);
  }
</style>
</head>
<body>
<svg class="dieline" viewBox="0 0 1200 1000" xmlns="http://www.w3.org/2000/svg">
  <g class="dust-flaps">
    <polygon class="board" points="491,49 451,84 451,232 491,264"/>
    <polygon class="board" points="708,49 748,81 748,228 708,264"/>
    <polygon class="board" points="491,264 451,298 451,447 491,479"/>
    <polygon class="board" points="708,264 748,296 748,443 708,479"/>
    <polygon class="board" points="491,694 451,729 451,878 491,907"/>
    <polygon class="board" points="708,694 748,727 748,873 708,907"/>
  </g>

  <g class="panels">
    <rect class="board panel-top" x="491" y="49" width="217" height="215"/>
    <rect class="board panel-back" x="491" y="264" width="217" height="215"/>
    <rect class="board panel-base" x="491" y="479" width="217" height="215"/>
    <rect class="board panel-front" x="491" y="694" width="217" height="213"/>
    <rect class="board side-left" x="276" y="479" width="215" height="215"/>
    <rect class="board side-right" x="708" y="479" width="214" height="215"/>
    <polygon class="board tuck-tab" points="493,907 706,907 676,952 527,952"/>
  </g>

  <g class="folds">
    <line class="fold-line" x1="491" y1="49" x2="491" y2="907"/>
    <line class="fold-line" x1="708" y1="49" x2="708" y2="907"/>
    <line class="fold-line" x1="491" y1="264" x2="708" y2="264"/>
    <line class="fold-line" x1="491" y1="479" x2="708" y2="479"/>
    <line class="fold-line" x1="491" y1="694" x2="708" y2="694"/>
    <line class="fold-line" x1="491" y1="907" x2="708" y2="907"/>
  </g>

  <g class="side-accents">
    <line class="gold-rule" x1="451" y1="479" x2="451" y2="694"/>
    <line class="gold-rule" x1="749" y1="479" x2="749" y2="694"/>
  </g>

  <g class="lid-label">
    <circle class="brand-mark-dot" cx="599" cy="100" r="18"/>
    <text class="brand-name" x="599" y="163" text-anchor="middle">Dawn Meadow</text>
    <text class="product-name" x="599" y="208" text-anchor="middle">under eye cream</text>
    <line class="gold-rule" x1="491" y1="221" x2="708" y2="221"/>
    <text class="net-weight" x="599" y="247" text-anchor="middle">0.5 oz</text>
  </g>

  <g class="front-label">
    <text class="brand-name" x="599" y="806" text-anchor="middle">Dawn Meadow</text>
  </g>
</svg>
</body>
</html>
```